For Sale Sign for Real Estate Agency

We need a For Sale Sign designed for our agency. I want a very simple/elegant sign that says "For Sale" towards the top of the sign (not in huge letters). Most of the sign should be a design/picture with our name and phone number somewhere at the bottom.

One significant detail, it's important that our logo not be too big or the center piece of the sign. Since our company name has the word "rent" in it, people assume the house is for rent, instead of for sale.

I attached our logo and a rough outline of the format I'm looking for.

Again, I'm looking for elegant and simple! Thanks for your time

Industry/Entity Type

Real Estate

Colors

Designer to choose colors to be used in the design.

Requirements
Must have
Nice to have
Should not have
• Nothing tacky!
• Our logo/company name should not be too big or the center piece of the sign. Since our company name has the word "rent" in it, people assume the house is for rent, instead of for sale.

```html
<!DOCTYPE html>
<html lang="en">
<head>
<meta charset="UTF-8">
<title>For Sale Sign – Larkfield Realty</title>
<link rel="stylesheet" href="https://fonts.googleapis.com/css2?family=Montserrat:wght@400;600&display=swap">
<style>
  :root {
    --backdrop: #eceef2;
    --sign-navy: #201f50;
    --sign-ink: #ffffff;
  }
  * { margin: 0; padding: 0; box-sizing: border-box; }
  html, body {
    width: 1200px;
    height: 960px;
    overflow: hidden;
    background: var(--backdrop);
  }
  .canvas {
    width: 1200px;
    height: 960px;
    display: flex;
    align-items: center;
    justify-content: center;
  }
  .sign-panel {
    position: relative;
    width: 660px;
    height: 880px;
    background: var(--sign-navy);
    color: var(--sign-ink);
    font-family: "Montserrat", sans-serif;
  }
  .sign-heading {
    position: absolute;
    top: 102px;
    left: 0;
    right: 0;
    text-align: center;
    font-weight: 600;
    font-size: 78px;
    letter-spacing: 3px;
    line-height: 1;
  }
  .agency-mark {
    position: absolute;
    top: 470px;
    left: 50%;
    transform: translateX(-50%);
    display: flex;
    align-items: center;
    gap: 22px;
  }
  .agency-mark__square {
    width: 58px;
    height: 58px;
    border: 4px solid var(--sign-ink);
    flex: none;
  }
  .agency-name {
    display: flex;
    flex-direction: column;
    align-items: flex-end;
    font-weight: 400;
    line-height: 1;
  }
  .agency-name__main {
    font-size: 60px;
    letter-spacing: -1px;
  }
  .agency-name__sub {
    font-size: 34px;
    letter-spacing: 8px;
    margin-top: 12px;
    margin-right: -8px;
  }
  .sign-contact {
    position: absolute;
    top: 740px;
    left: 0;
    right: 0;
    display: flex;
    align-items: center;
    justify-content: center;
    gap: 18px;
    font-weight: 600;
    font-size: 56px;
    letter-spacing: 2px;
    line-height: 1;
  }
  .sign-contact__icon {
    width: 46px;
    height: 46px;
    flex: none;
  }
</style>
</head>
<body>
  <main class="canvas">
    <section class="sign-panel">
      <h1 class="sign-heading">FOR SALE</h1>

      <div class="agency-mark">
        <span class="agency-mark__square" aria-hidden="true"></span>
        <p class="agency-name">
          <span class="agency-name__main">Larkfield</span>
          <span class="agency-name__sub">Realty</span>
        </p>
      </div>

      <p class="sign-contact">
        <svg class="sign-contact__icon" viewBox="0 0 46 46" aria-hidden="true">
          <circle cx="23" cy="23" r="20" fill="none" stroke="currentColor" stroke-width="3"/>
          <path d="M16 13c1.5-1 3-.5 3.6.8l1.6 3.4c.5 1.1.1 2.2-.9 2.9l-1.3.9c1 2.6 3 4.8 5.5 6.2l1-1.2c.8-1 2-1.2 3-.6l3.2 1.9c1.2.7 1.5 2.2.6 3.5l-1 1.4c-1 1.4-2.8 1.9-4.5 1.3C20.6 31.9 14.6 25.8 13 19.1c-.4-1.7.2-3.4 1.6-4.5z" fill="none" stroke="currentColor" stroke-width="2.2" stroke-linejoin="round"/>
        </svg>
        <span class="sign-contact__number">555-210-4477</span>
      </p>
    </section>
  </main>
</body>
</html>
```